Flyer for IT Services

We need a flyer template for our different products and services we offer. We're an IT firm that provides Managed Services, Remote Backup, Mobile Device Management, Unified Communications, and more.

The flyer should be two sided and provide an area for an explanation of the service and then some pictures, lists of features, and a section for our contact info and company description.

We will normally send the flyer over to a client as a PDF via email but may also printer the flyers to hand out at meetings with prospects.

Information on the services to get ideas is at the following and the services heading:
www.tanfernsys.example

Target Market(s)

small to medium sized companies (2-150 employees)

Industry/Entity Type

Printer

Requirements
Must have
• Flyer must be two sided, include our logo, and have sections for product and company description as well as feature lists.

```html
<!DOCTYPE html>
<html lang="en">
<head>
<meta charset="utf-8">
<title>TFS – IT Consulting Flyer, Front</title>
<link rel="stylesheet" href="https://fonts.googleapis.com/css2?family=Cinzel:wght@400;600&family=Mulish:wght@500;700;800&display=swap">
<style>
  :root {
    --page: #ffffff;
    --teal: #6cf3e2;
    --teal-light: #8ef7ea;
    --teal-label: #62ecd9;
    --tagline: #5e9ea6;
    --white: #ffffff;
    --photo-light: #eef2f3;
    --photo-mid: #c9d3d6;
    --photo-dark: #6f7a80;
  }
  * { margin: 0; padding: 0; box-sizing: border-box; }
  html, body {
    width: 1200px; height: 900px; overflow: hidden;
    background: var(--page);
    font-family: "Mulish", "Century Gothic", sans-serif;
  }
  .canvas { position: relative; width: 1200px; height: 900px; }

  .flyer {
    position: absolute; left: 52px; top: 48px;
    width: 1095px; height: 707px; overflow: hidden;
  }
  .flyer__photo {
    position: absolute; left: 0; top: 0; width: 698px; height: 707px;
    background:
      radial-gradient(ellipse at 30% 70%, var(--photo-dark) 0%, rgba(111,122,128,0.35) 35%, transparent 60%),
      linear-gradient(160deg, var(--photo-light) 0%, #dde5e7 40%, var(--photo-mid) 100%);
  }
  .flyer__panel { position: absolute; left: 0; top: 0; width: 1095px; height: 707px; }

  .tagline {
    position: absolute; left: 338px; top: 40px;
    font-family: "Cinzel", "Trajan Pro", serif;
    font-size: 19px; line-height: 23px; letter-spacing: 0.5px;
    color: var(--tagline);
  }

  .brand {
    position: absolute; right: 18px; top: 18px;
    display: flex; align-items: center; gap: 10px;
    color: var(--white);
  }
  .brand__dot {
    width: 36px; height: 36px; border-radius: 50%;
    border: 3px solid var(--white);
  }
  .brand__name { font-size: 44px; font-weight: 800; letter-spacing: 2px; line-height: 1; }
  .brand__web {
    position: absolute; right: 18px; top: 80px;
    font-size: 16.5px; font-weight: 700; color: var(--white);
  }

  .service-title {
    position: absolute; left: 624px; top: 288px;
    font-size: 60px; font-weight: 800; line-height: 62px;
    color: var(--white); letter-spacing: 1px;
  }

  .service-copy {
    position: absolute; left: 723px; top: 526px; width: 352px;
    font-size: 15.5px; font-weight: 500; line-height: 22.5px;
    color: var(--white);
  }

  .side-label {
    position: absolute; right: 54px; top: 798px;
    font-size: 64px; font-weight: 500; line-height: 1;
    color: var(--teal-label); letter-spacing: 1px;
  }
</style>
</head>
<body>
<main class="canvas">
  <section class="flyer">
    <div class="flyer__photo" role="img" aria-label="Photo of two business colleagues reviewing a phone and laptop in a bright office"></div>

    <svg class="flyer__panel" viewBox="0 0 1095 707" aria-hidden="true">
      <defs>
        <linearGradient id="panelTone" x1="0" y1="0" x2="1" y2="1">
          <stop offset="0" stop-color="var(--teal-light)"/>
          <stop offset="1" stop-color="var(--teal)"/>
        </linearGradient>
      </defs>
      <path d="M698 0 H1095 V707 H698 V503 A148 148 0 0 1 698 207 Z" fill="url(#panelTone)"/>
    </svg>

    <p class="tagline">Using technology as a tool<br>to solve business challenges</p>

    <div class="brand">
      <span class="brand__dot"></span>
      <span class="brand__name">TFS</span>
    </div>
    <p class="brand__web">www.tanfernsys.example</p>

    <h1 class="service-title">IT<br>CONSULTING</h1>

    <p class="service-copy">When it comes to the technology you need to run your business, it's hard to make sense of all the options. Tanfern Systems does more than just sell technology -We combine IT and small business consulting expertise to develop technology solutions to your real business challenges.</p>
  </section>

  <p class="side-label">FRONT</p>
</main>
</body>
</html>
```